Wordpress website design for a high-end painting business

We are currently rebranding and are looking to update our Wordpress theme. We have recently rebranded our logo on ArtHatchery, and would like our website to be equally as refined.
Our business is named “Holloway Coatings”. We are a high-end painting business that is known for being professional and having high standards. Our clean and professional image is important as it separates us from our competition. Our current website can be found at www.hollowayfinishes.co.nz . We designed the site ourselves so it is understandably rudimentary. We are generally happy with the. page layout of our existing site, but we like a professional remodel. Any ideas on improvement welcomed.
We would like the front page of the website to summarise all of the info throughout the whole website (I.e introduction, photos, testimonials, contact info etc.) as visitors typically scroll through the first page to see that we are reputable and get to our contact number/email contact at the bottom of the page. We would like this first page to give a clean well rounded image of our business. We would like the gallery to be a scroll through of large photos, as it is difficult to see paint details in smaller photos. A contact page with an enquiry section would also be good.
For the colour scheme, we would like something that fits a bold, masculine and high end theme (similar to our logo attached).
We would like the footer to include Velnor paint logos and the accredited painter logo we have included as these are important to our profession.
We have attached some photos of our work also. I will add more in the coming days. More can also be found on our website.
If you have questions or comments, please don’t hesitate to ask and I will get back as soon as possible.
We are open to your own interpretation or ideas for a better layout/site provided they fit the general brief of being a well rounded site for our profession.
Thanks,
Holloway Coatings.
Target Market(s)
High end clients
Industry/Entity Type
Painting (interior and exterior)
Coding
Coded - Design and coding required
Requirements
Must have
- Classy feel, separating us from typical painting companies. Well rounded homepage.
Nice to have
- Lots of examples of our work
Should not have
- Untidy paint motifs (eg, paint droplets, paint splashes)

```html
<!DOCTYPE html>
<html lang="en">
<head>
<meta charset="utf-8">
<title>Holloway Coatings</title>
<link href="https://fonts.googleapis.com/css2?family=Playfair+Display:wght@700;900&family=Poppins:ital,wght@0,400;0,500;0,600;0,700;1,400&display=swap" rel="stylesheet">
<style>
:root{
  --brown:#8c6a47;
  --brown-dark:#7a5b3c;
  --navy:#1b2230;
  --ink:#1d1f26;
  --text:#4a4d55;
  --mist:#eceef2;
  --cream:#e6dfd6;
  --white:#fff;
  --line:#d7d9de;
}
*{box-sizing:border-box;margin:0;padding:0}
html,body{width:1200px;height:3658px;overflow:hidden;background:var(--white)}
body{position:relative;font-family:'Poppins',sans-serif;color:var(--text)}
.abs{position:absolute}
.serif{font-family:'Playfair Display',serif;color:var(--ink)}
.btn{position:absolute;display:flex;align-items:center;justify-content:center;font-weight:700;font-size:11.5px;letter-spacing:.3px;text-transform:uppercase;background:var(--brown);color:var(--white)}
.photo{position:absolute;border-radius:50%;overflow:hidden}
.brand{position:absolute;display:flex;align-items:center;gap:14px}
.brand-dot{border-radius:50%;background:var(--navy)}
.brand-name{font-family:'Playfair Display',serif;font-weight:700;color:var(--navy);line-height:1.05;letter-spacing:1px}
.nav{position:absolute;right:88px;top:58px;display:flex;gap:19px;font-size:13px;font-weight:600;color:var(--ink);text-transform:uppercase}
.nav .active{color:var(--brown)}
.label{font-size:11.5px;font-weight:700;color:var(--ink);text-transform:uppercase}
.gallery-item{position:absolute;top:2022px;width:246px;height:328px;border-radius:4px}
.quote-card{position:absolute;top:2530px;width:390px}
.quote-mark{font-family:'Playfair Display',serif;font-size:120px;color:#e3e4e8;line-height:1;position:absolute;top:-10px;left:165px}
.quote-text{font-style:italic;font-size:15px;line-height:24px;color:var(--text);padding-top:60px}
.author{display:flex;align-items:center;gap:16px;margin-top:26px}
.avatar{width:68px;height:68px;border-radius:50%}
.author b{display:block;font-size:14.5px;color:var(--ink);text-transform:uppercase}
.author span{font-size:13px;color:#a3a6ad;font-weight:600}
.foot-h{font-family:'Playfair Display',serif;font-weight:700;font-size:17px;color:var(--ink);text-transform:uppercase;letter-spacing:.3px}
.foot-list{list-style:none;font-size:14px;color:var(--text)}
.foot-list li{height:31px}
.foot-list li::before{content:"›";color:var(--brown);margin-right:10px}
</style>
</head>
<body>

<!-- Hero backdrop -->
<svg class="abs" style="left:0;top:0" width="1200" height="720" viewBox="0 0 1200 720">
  <path d="M520 0 H1200 V470 C1150 380 1060 330 960 300 C780 250 600 240 530 120 C510 80 510 30 520 0Z" fill="var(--mist)"/>
</svg>

<header>
  <div class="brand" style="left:88px;top:26px">
    <div class="brand-dot" style="width:96px;height:96px"></div>
    <div class="brand-name" style="font-size:22px">HOLLOWAY<br>COATINGS</div>
  </div>
  <nav class="nav">
    <span class="active">Home</span><span>Services</span><span>Gallery</span><span>About</span><span>Testimonials</span><span>Contact</span>
  </nav>
  <div class="abs" style="left:651px;top:0;width:44px;height:3px;background:var(--brown)"></div>
</header>

<section class="hero">
  <div class="label abs" style="left:88px;top:297px">Welcome Holloway Coatings</div>
  <div class="abs" style="left:287px;top:303px;width:200px;height:2px;background:var(--brown)"></div>
  <h1 class="serif abs" style="left:86px;top:326px;font-weight:900;font-size:74px;line-height:72px;letter-spacing:-.5px">ALWAYS ON<br>TARGET</h1>
  <p class="abs" style="left:87px;top:483px;width:380px;font-size:17px;line-height:27px">Here at Holloway Coatings, we take a lot of pride in our work.</p>
  <div class="btn" style="left:88px;top:561px;width:182px;height:44px">View our projects</div>
  <div class="photo" role="img" aria-label="Photo of a two-storey beige house with brown roof and rose garden" style="left:588px;top:128px;width:544px;height:544px;background:linear-gradient(180deg,#8fb6e4 0%,#c9b79c 45%,#a59580 65%,#6e8c4a 100%);box-shadow:0 30px 60px rgba(0,0,0,.08)"></div>
</section>

<section class="about">
  <div class="photo" role="img" aria-label="Photo of a freshly painted cream house with grey roof" style="left:87px;top:722px;width:478px;height:478px;background:linear-gradient(180deg,#c7ccd2 0%,#b5b3a7 45%,#8a8778 62%,#5d8a3a 100%)"></div>
  <div class="photo" role="img" aria-label="Photo of a brick house with painted gables" style="left:418px;top:998px;width:220px;height:220px;border:6px solid var(--white);background:linear-gradient(180deg,#7fa9df 0%,#cfd6de 45%,#8a5140 70%,#5f7d3b 100%)"></div>
  <div class="abs" style="left:709px;top:800px;width:30px;height:2px;background:var(--brown)"></div>
  <div class="label abs" style="left:748px;top:794px">Introduction</div>
  <h2 class="serif abs" style="left:708px;top:812px;font-weight:700;font-size:41px">ABOUT US</h2>
  <p class="abs" style="left:709px;top:869px;width:405px;font-size:14.2px;line-height:22.3px">Here at Holloway Coatings, we take a lot of pride in our work. We strive to ensure the highest quality paint-work, paying close attention to detail to provide a long lasting finish. Our clients are always our priority, we aim to deliver beyond their expectations. It is our goal to provide an excellent service from start to finish through clear communication, free quoting and transparency with our pricing.</p>
  <div class="btn" style="left:709px;top:1071px;width:113px;height:33px">Read more</div>
</section>

<section class="services">
  <svg class="abs" style="left:0;top:1225px" width="1200" height="582" viewBox="0 0 1200 582">
    <path d="M0 150 C120 200 280 230 420 150 C560 70 660 20 820 10 C1000 0 1120 60 1200 170 V582 H0Z" fill="var(--cream)"/>
    <path d="M0 155 C140 225 300 230 440 160 C580 90 680 10 880 8 C1030 6 1130 80 1200 170 V582 H0Z" fill="var(--brown)"/>
    <circle cx="713" cy="177" r="26" fill="#a98a69"/>
    <circle cx="872" cy="470" r="25" fill="#a98a69"/>
  </svg>
  <h2 class="serif abs" style="left:154px;top:1530px;font-weight:700;font-size:41px;color:var(--white)">OUR SERVICES</h2>
  <p class="abs" style="left:155px;top:1590px;width:420px;font-size:17.5px;line-height:27px;color:var(--white)">We proudly use the finest quality Velnor paints on all of the projects that we work on.</p>
  <div class="btn" style="left:155px;top:1670px;width:112px;height:32px;background:var(--white);color:var(--ink)">Read more</div>

  <div class="abs" style="left:782px;top:1310px;width:256px;height:256px;border-radius:50%;background:var(--white);box-shadow:6px 6px 0 #a98a69"></div>
  <svg class="abs" style="left:865px;top:1368px" width="94" height="88" viewBox="0 0 94 88" fill="none" stroke="var(--ink)" stroke-width="2.5">
    <path d="M4 22 L12 2 L20 22Z" stroke="var(--brown)"/><line x1="12" y1="22" x2="12" y2="86"/>
    <rect x="52" y="2" width="38" height="84"/><rect x="60" y="10" width="10" height="14"/><rect x="72" y="10" width="10" height="14"/>
    <path d="M28 44 Q28 32 46 32 Q64 32 64 44 V70 H28Z"/><rect x="22" y="52" width="48" height="18"/><line x1="28" y1="70" x2="26" y2="80"/><line x1="64" y1="70" x2="66" y2="80"/>
  </svg>
  <div class="serif abs" style="left:782px;top:1468px;width:256px;text-align:center;font-size:19px;line-height:27px;font-weight:700">INTERIOR<br>SERVICE</div>

  <div class="abs" style="left:621px;top:1473px;width:272px;height:272px;border-radius:50%;background:var(--white)"></div>
  <svg class="abs" style="left:694px;top:1540px" width="106" height="88" viewBox="0 0 106 88" fill="none" stroke="var(--ink)" stroke-width="2.5">
    <path d="M2 30 L30 2 H76 L104 30"/><rect x="6" y="30" width="94" height="56"/>
    <rect x="16" y="38" width="12" height="12"/><rect x="36" y="38" width="12" height="12"/><rect x="58" y="38" width="12" height="12"/><rect x="78" y="38" width="12" height="12"/>
    <rect x="22" y="58" width="22" height="28"/><rect x="60" y="58" width="36" height="26" stroke="var(--brown)"/><line x1="60" y1="67" x2="96" y2="67" stroke="var(--brown)"/><line x1="60" y1="76" x2="96" y2="76" stroke="var(--brown)"/>
  </svg>
  <div class="serif abs" style="left:621px;top:1647px;width:250px;text-align:center;font-size:19px;line-height:27px;font-weight:700">EXTERIOR<br>SERVICE</div>
</section>

<section class="gallery">
  <h2 class="serif abs" style="left:0;top:1902px;width:1200px;text-align:center;font-weight:700;font-size:41px">OUR GALLERY</h2>
  <p class="abs" style="left:0;top:1960px;width:1200px;text-align:center;font-size:17.5px">Examples of our work: Exterior repaint in Ferndale, Westvale.</p>
  <div class="gallery-item" role="img" aria-label="Photo of a painted living room with blue carpet and sofa" style="left:88px;background:linear-gradient(180deg,#e9ece8 0%,#d8d6cd 55%,#2f4677 80%,#23345c 100%)"></div>
  <div class="gallery-item" role="img" aria-label="Photo of a freshly painted kitchen with island bench" style="left:346px;background:linear-gradient(180deg,#eceae6 0%,#d6d1c8 50%,#8a5a3a 85%,#6d4428 100%)"></div>
  <div class="gallery-item" role="img" aria-label="Photo of a white kitchen with range hood" style="left:605px;background:linear-gradient(180deg,#f3f1ec 0%,#e2ddd4 55%,#b9b3aa 80%,#8d877d 100%)"></div>
  <div class="gallery-item" role="img" aria-label="Photo of a painter working on a ceiling" style="left:863px;background:linear-gradient(180deg,#f1ece5 0%,#dfd1c1 50%,#c8b49e 80%,#a99580 100%)"></div>
</section>

<section class="testimonials">
  <h2 class="serif abs" style="left:0;top:2444px;width:1200px;text-align:center;font-weight:700;font-size:41px">TESTIMONIALS</h2>
  <div class="quote-card" style="left:89px">
    <div class="quote-mark">“</div>
    <p class="quote-text">Very happy with Holloway decorators. Rowan and Eli did a great job with good communication and attention to detail. Definitely recommend… good value for money!</p>
    <div class="author"><div class="avatar" role="img" aria-label="Client portrait" style="background:linear-gradient(135deg,#9aa7b3,#3b4450)"></div><div><b>Warren Blake</b><span>(2020)</span></div></div>
  </div>
  <div class="quote-card" style="left:546px">
    <div class="quote-mark">“</div>
    <p class="quote-text">Rowan and Eli was prompt and efficient. Very friendly and knowledgeable. Everything was done better than I expected. I would highly recommend them for anyone looking for painters.</p>
    <div class="author"><div class="avatar" role="img" aria-label="Client portrait" style="background:linear-gradient(135deg,#d9d9d9,#6c6760)"></div><div><b>Dorian Hale</b><span>(2020)</span></div></div>
  </div>
  <div class="quote-card" style="left:998px;width:420px">
    <div class="quote-mark">“</div>
    <p class="quote-text">We could not be happier with the painting the exterior of our home. Rowan and Eli had brilliant communication and it went very smoothly. Would recommend.</p>
    <div class="author"><div class="avatar" role="img" aria-label="Client portrait" style="background:linear-gradient(135deg,#e7cdb3,#7a5237)"></div><div><b>Tessa Morrow</b><span>(2020)</span></div></div>
  </div>
</section>

<section class="newsletter">
  <svg class="abs" style="left:0;top:2815px" width="1200" height="425" viewBox="0 0 1200 425">
    <path d="M0 150 C80 60 200 5 340 5 C470 5 560 60 650 110 C760 170 880 200 1010 175 C1100 158 1160 125 1200 100 V425 H0Z" fill="var(--line)"/>
    <path d="M0 160 C80 65 200 8 340 8 C470 8 560 65 650 118 C760 180 880 210 1010 185 C1100 168 1160 135 1200 110 V425 H0Z" fill="var(--navy)"/>
  </svg>
  <h2 class="serif abs" style="left:96px;top:2985px;font-weight:700;font-size:41px;line-height:46px;color:var(--white)">SUBSCRIBE OUR<br>NEWSLETTER</h2>
  <p class="abs" style="left:96px;top:3096px;width:330px;font-size:17.5px;line-height:25px;color:var(--white)">Join our subscribers list go get the latest news.</p>
  <div class="abs" style="left:511px;top:3100px;width:598px;height:58px;background:var(--white);display:flex;align-items:center">
    <svg style="margin-left:27px" width="16" height="12" viewBox="0 0 16 12"><rect width="16" height="12" fill="#b5b8bf"/><path d="M0 0 L8 7 L16 0" stroke="#fff" stroke-width="1.5" fill="none"/></svg>
    <span style="margin-left:11px;font-size:15.5px;color:#5b5e66">Enter your email address...</span>
    <div class="btn" style="right:4px;top:4px;width:120px;height:50px">Subscribe</div>
  </div>
</section>

<footer>
  <div class="brand" style="left:128px;top:3330px;flex-direction:column;gap:12px">
    <div class="brand-dot" style="width:150px;height:150px"></div>
    <div class="brand-name" style="font-size:22px;text-align:center">HOLLOWAY<br>COATINGS</div>
  </div>
  <div class="foot-h abs" style="left:355px;top:3310px">Quick links</div>
  <ul class="foot-list abs" style="left:356px;top:3358px">
    <li>Home</li><li>About Us</li><li>Our Gallery</li><li>About Us</li><li>Testimonials</li><li>Contact Us</li>
  </ul>
  <div class="foot-h abs" style="left:545px;top:3310px">Contact info</div>
  <div class="abs" style="left:545px;top:3356px;font-size:14px;line-height:19px;color:var(--text);width:240px">
    <div>Eli Varnsworth</div>
    <div style="margin-top:16px;padding-left:23px;position:relative"><svg style="position:absolute;left:0;top:4px" width="13" height="10" viewBox="0 0 13 10"><rect width="13" height="10" fill="var(--brown)"/><path d="M0 0 L6.5 5 L13 0" stroke="#fff" stroke-width="1.2" fill="none"/></svg>Email:<br>hello@hollowaycoatings.example</div>
    <div style="margin-top:16px;padding-left:23px;position:relative"><svg style="position:absolute;left:0;top:2px" width="13" height="13" viewBox="0 0 24 24"><path fill="var(--brown)" d="M6.6 10.8a15 15 0 0 0 6.6 6.6l2.2-2.2c.3-.3.7-.4 1-.2 1.1.4 2.3.6 3.6.6.6 0 1 .4 1 1V20c0 .6-.4 1-1 1A17 17 0 0 1 3 4c0-.6.4-1 1-1h3.5c.6 0 1 .4 1 1 0 1.3.2 2.5.6 3.6.1.3 0 .7-.2 1z"/></svg>Phone:<br>021 555 0192</div>
    <div style="margin-top:18px">Ashbury, Westvale.</div>
  </div>
  <div class="foot-h abs" style="left:819px;top:3310px">Proudly sponsored by</div>
  <div class="abs" role="img" aria-label="Velnor partner badge" style="left:819px;top:3364px;width:112px;height:36px;background:#1c2a6b"></div>
  <div class="abs" role="img" aria-label="Accredited painter badge" style="left:819px;top:3414px;width:202px;height:32px;background:#1e9ad6"></div>
  <div class="abs" style="left:88px;top:3603px;width:1024px;height:1px;background:var(--line)"></div>
  <div class="abs" style="left:0;top:3624px;width:1200px;text-align:center;font-size:11.5px;font-weight:600;color:var(--ink)">2022 © HOLLOWAYCOATINGS. ALL RIGHTS RESERVED</div>
  <div class="abs" style="left:1132px;top:3581px;width:42px;height:42px;border-radius:50%;background:var(--brown);display:flex;align-items:center;justify-content:center">
    <svg width="12" height="14" viewBox="0 0 12 14"><path d="M6 13 V2 M1.5 6 L6 1.5 L10.5 6" stroke="#fff" stroke-width="1.5" fill="none"/></svg>
  </div>
</footer>

</body>
</html>
```